Floor Inspections and Consulting

We provide inspections and consulting services on various floor coverings, e.g. carpet, hardwood, etc. We also do expert witness work for attorneys due to floor covering failures. We current have a logo, just need it incorporated into a new design. I have examples of cards I have found on the internet that capture my attention and make a statement. I have included our original business card, which in my opinion is terrible, but it does have our logo on it.

```html
<!DOCTYPE html>
<html lang="en">
<head>
<meta charset="utf-8">
<title>Groundline Inspections – Business Card</title>
<link href="https://fonts.googleapis.com/css2?family=Open+Sans:wght@400;600;700&family=Source+Code+Pro:wght@500&display=swap" rel="stylesheet">
<style>
  :root{
    --canvas:#1b1b1c;
    --card-dark:#120b0a;
    --brown:#5b3b1f;
    --brown-bar:#5a3520;
    --wine:#2b1410;
    --edge:#3a2114;
    --icon-box:#2a1812;
    --ink:#f3eee8;
    --founder:#6a4424;
  }
  *{margin:0;padding:0;box-sizing:border-box}
  html,body{width:1200px;height:800px;overflow:hidden;background:var(--canvas)}
  .canvas{position:relative;width:1200px;height:800px;display:flex;align-items:center;justify-content:center;gap:40px}
  .card{position:relative;width:560px;height:320px;overflow:hidden;background:var(--card-dark);font-family:"Open Sans",sans-serif;color:var(--ink)}
  .card-shapes{position:absolute;inset:0;width:100%;height:100%}

  /* back side */
  .back-name{position:absolute;left:180px;top:95px;width:200px;text-align:center;font-weight:700;font-size:28px;line-height:1.2;color:var(--ink);letter-spacing:.5px}
  .back-tagline{position:absolute;left:0;width:100%;top:268px;text-align:center;font-family:"Source Code Pro",monospace;font-size:13px;letter-spacing:2px;color:var(--ink)}

  /* front side */
  .front-name-mark{position:absolute;left:40px;top:118px;width:220px;text-align:center;font-weight:700;font-size:26px;line-height:1.2;color:var(--ink)}
  .person{position:absolute;right:56px;top:34px;text-align:right}
  .person-name{font-weight:700;font-size:28px;line-height:1;color:var(--ink);letter-spacing:.3px;white-space:nowrap}
  .person-role{margin-top:6px;font-size:11px;letter-spacing:5px;color:var(--founder);white-space:nowrap;margin-right:-5px}
  .person-icon{position:absolute;right:26px;top:52px}
  .contact-list{position:absolute;left:298px;top:112px;list-style:none}
  .contact-row{display:flex;align-items:center;height:28px;margin-bottom:12px}
  .contact-icon{flex:none;width:32px;height:28px;background:var(--icon-box);display:flex;align-items:center;justify-content:center}
  .contact-text{height:24px;min-width:200px;background:var(--brown-bar);font-size:12.5px;line-height:24px;padding:0 8px;white-space:nowrap}
  .front-tagline{position:absolute;left:312px;top:254px;font-family:"Source Code Pro",monospace;font-size:14px;letter-spacing:2px;color:var(--ink);white-space:nowrap}
</style>
</head>
<body>
<main class="canvas">

  <section class="card card-back" aria-label="Card back">
    <svg class="card-shapes" viewBox="0 0 560 320" aria-hidden="true">
      <rect width="560" height="320" fill="var(--card-dark)"/>
      <rect x="0" y="0" width="560" height="14" fill="var(--brown)"/>
      <rect x="0" y="14" width="220" height="8" fill="var(--wine)"/>
      <rect x="0" y="302" width="560" height="18" fill="var(--brown)"/>
      <polygon points="10,122 150,122 150,146 14,146" fill="var(--brown)"/>
      <polygon points="14,154 156,154 160,178 18,178" fill="var(--wine)"/>
      <polygon points="18,186 166,186 172,210 22,210" fill="var(--brown)"/>
      <polygon points="412,110 552,110 548,134 406,134" fill="var(--brown)"/>
      <polygon points="404,142 548,142 544,166 398,166" fill="var(--wine)"/>
      <polygon points="398,174 544,174 540,198 394,198" fill="var(--brown)"/>
      <circle cx="280" cy="152" r="148" fill="#0d0706"/>
      <circle cx="280" cy="152" r="134" fill="var(--brown)"/>
    </svg>
    <p class="back-name">Groundline Inspections</p>
    <p class="back-tagline">ANALYSIS &amp; CONSULTING</p>
  </section>

  <section class="card card-front" aria-label="Card front">
    <svg class="card-shapes" viewBox="0 0 560 320" aria-hidden="true">
      <rect width="560" height="320" fill="var(--card-dark)"/>
      <rect x="0" y="0" width="560" height="12" fill="var(--edge)"/>
      <rect x="0" y="304" width="560" height="16" fill="var(--edge)"/>
      <path d="M0,0 L150,0 A160,160 0 0 1 150,320 L0,320 Z" fill="var(--brown)"/>
    </svg>
    <p class="front-name-mark">Groundline Inspections</p>

    <div class="person">
      <h1 class="person-name">Daniel Marsh</h1>
      <p class="person-role">FOUNDER</p>
    </div>
    <svg class="person-icon" width="22" height="26" viewBox="0 0 22 26" aria-hidden="true">
      <circle cx="11" cy="7" r="6" fill="var(--ink)"/>
      <path d="M0,26 Q0,14 11,14 Q22,14 22,26 Z" fill="var(--ink)"/>
    </svg>

    <ul class="contact-list">
      <li class="contact-row">
        <span class="contact-icon">
          <svg width="14" height="16" viewBox="0 0 14 16" aria-hidden="true"><path d="M3,0 L6,4 L4,6 Q6,10 9,12 L11,10 L14,13 L11,16 Q1,12 0,3 Z" fill="var(--ink)"/></svg>
        </span>
        <span class="contact-text">303-555-0142</span>
      </li>
      <li class="contact-row">
        <span class="contact-icon">
          <svg width="18" height="18" viewBox="0 0 18 18" aria-hidden="true" fill="none" stroke="var(--ink)" stroke-width="1.4"><circle cx="9" cy="9" r="7.5"/><ellipse cx="9" cy="9" rx="3.2" ry="7.5"/><line x1="1.5" y1="9" x2="16.5" y2="9"/></svg>
        </span>
        <span class="contact-text">Groundlineflooring.com</span>
      </li>
      <li class="contact-row">
        <span class="contact-icon">
          <svg width="18" height="18" viewBox="0 0 18 18" aria-hidden="true"><circle cx="9" cy="9" r="8" fill="var(--ink)"/><text x="9" y="13" text-anchor="middle" font-family="Open Sans, sans-serif" font-size="12" font-weight="700" fill="var(--icon-box)">@</text></svg>
        </span>
        <span class="contact-text">Daniel@groundlineflooring.com</span>
      </li>
    </ul>

    <p class="front-tagline">ANALYSIS &amp; CONSULTING</p>
  </section>

</main>
</body>
</html>
```